Diverse, up-scale salon needs eye-catching, unique business cards.

We are looking for a unique business card design for our stylist but that can also be multi functional and used for appointment reminder and referrals. I will need a design in a format that I can modify names and titles going forward. In the past we have had a dark background with the logo on one side, and stylist and contact information on the other but we are open to all ideas. I have included our mission statement as well as branded colors below. The statement doesn't need to go on the card, it's just a reference for target market. We need space for the stylists name, title, instagram handle and then the salons phone number, website and address. I am also open to adding a spot for a qr code linked to the stylist instagram or the salon booking link.

primary brand colors:
#333333 #233415 #36502a #93874a #000000
Mission statement:
Venturo Mane Studio, a high-end salon located in the lively Downtown Farmington, Michigan, is committed to providing exceptional services in a welcoming and relaxed environment to meet the needs of our diverse clientele.
Our salon specializes in contemporary custom haircuts, coloring, extensions, and barbering and beard grooming services. Our team of skilled stylists is passionate and inventive in their hair styling techniques. At the heart of our salon are values centered on quality, innovation, creativity, and above all, comfort. These core values are evident in every appointment across our customizable array of services.
Our goal is to establish a benchmark for exceptional hair care for every human.
Website: www.venturomanestudio.example
instagram: @venturomanestudio
address: 18720 Willowcrest Blvd, Farmington MI
phone: 248-316-7408

Industry/Entity Type

Hair Salon

Contact Information for Business Card

Stylist name, title, phone, instagram, website, address, (optional qr code)

Requirements
Should not have
• Does not need mission statement on the card.

```html
<!DOCTYPE html>
<html lang="en">
<head>
<meta charset="utf-8">
<title>Venturo Mane Studio – Business Card</title>
<link href="https://fonts.googleapis.com/css2?family=Arimo:wght@400;700&display=swap" rel="stylesheet">
<style>
  :root {
    --backdrop: #2b2b2c;
    --card-white: #ffffff;
    --gold: #93874a;
    --ink-dark: #1b1c1e;
    --text-grey: #5f5f5f;
    --rule-grey: #a9a9a9;
    --white: #ffffff;
  }
  * { margin: 0; padding: 0; box-sizing: border-box; }
  html, body {
    width: 1200px; height: 1108px; overflow: hidden;
    background: var(--backdrop);
    font-family: "Arimo", Arial, sans-serif;
  }
  .canvas {
    position: relative; width: 1200px; height: 1108px;
    display: flex; justify-content: center; align-items: center; gap: 56px;
  }
  .card {
    position: relative; width: 440px; height: 760px;
    border-radius: 30px; overflow: hidden;
  }

  /* Front */
  .card-front {
    background: var(--card-white);
    display: flex; flex-direction: column; align-items: center;
    padding-top: 78px; color: var(--text-grey); text-align: center;
  }
  .brand-ring {
    width: 150px; height: 150px; border-radius: 50%;
    border: 4px solid var(--gold);
  }
  .brand-name {
    margin-top: 18px; font-size: 24px; font-weight: 700; color: var(--gold);
    letter-spacing: 1px;
  }
  .stylist-name {
    margin-top: 34px; font-size: 30px; font-weight: 700; color: var(--gold);
    letter-spacing: 0.5px;
  }
  .stylist-title { font-size: 24px; margin-top: 4px; }
  .icon-row {
    display: flex; align-items: center; gap: 10px; width: 320px; margin-top: 12px;
  }
  .icon-row .rule { flex: 1; height: 1px; background: var(--rule-grey); }
  .icon-chip {
    width: 34px; height: 34px; border-radius: 7px; background: var(--gold);
    display: flex; align-items: center; justify-content: center;
  }
  .contact-list { margin-top: 16px; font-size: 24px; line-height: 1.22; }
  .divider { width: 320px; height: 1px; background: var(--rule-grey); margin: 14px 0; }
  .address { font-size: 24px; line-height: 1.22; }

  /* Back */
  .card-back { background: var(--ink-dark); }
  .card-back .split { position: absolute; inset: 0; }
  .back-brand {
    position: absolute; top: 150px; left: 0; width: 100%; text-align: center;
  }
  .back-brand .brand-ring { margin: 0 auto; border-color: var(--white); width: 120px; height: 120px; }
  .back-brand .brand-name { color: var(--white); }
  .services {
    position: absolute; top: 470px; left: 0; width: 100%; text-align: center;
    color: var(--white); font-size: 24px; line-height: 1.25;
  }
  .services h2 {
    font-size: 23px; font-weight: 700; color: var(--gold); margin-bottom: 4px;
  }
  .services ul { list-style: none; }
  .services li::before {
    content: ""; display: inline-block; width: 8px; height: 8px; border-radius: 50%;
    background: var(--gold); margin-right: 8px; vertical-align: middle;
  }
</style>
</head>
<body>
<main class="canvas">
  <section class="card card-front">
    <div class="brand-ring"></div>
    <div class="brand-name">VENTURO MANE STUDIO</div>
    <div class="stylist-name">MARCUS HALE</div>
    <div class="stylist-title">Manager</div>
    <div class="icon-row">
      <span class="rule"></span>
      <span class="icon-chip">
        <svg width="20" height="20" viewBox="0 0 24 24" fill="none" stroke="#fff" stroke-width="2.2" stroke-linecap="round" stroke-linejoin="round">
          <path d="M5 3h4l2 5-3 2a11 11 0 0 0 6 6l2-3 5 2v4a2 2 0 0 1-2 2A18 18 0 0 1 3 5a2 2 0 0 1 2-2z"/>
        </svg>
      </span>
      <span class="icon-chip"></span>
      <span class="icon-chip">
        <svg width="20" height="20" viewBox="0 0 24 24" fill="none" stroke="#fff" stroke-width="2">
          <circle cx="12" cy="12" r="9"/><path d="M3 12h18M12 3c3 3 3 15 0 18M12 3c-3 3-3 15 0 18"/>
        </svg>
      </span>
      <span class="rule"></span>
    </div>
    <div class="contact-list">
      <p>248-316-7408</p>
      <p>@venturomanestudio</p>
      <p>www.venturomanestudio.example</p>
    </div>
    <div class="divider"></div>
    <div class="address">
      <p>18720 Willowcrest Blvd</p>
      <p>Farmington MI</p>
    </div>
  </section>

  <section class="card card-back">
    <svg class="split" width="440" height="760" viewBox="0 0 440 760" aria-hidden="true">
      <path d="M0 0H440V340C330 300 160 230 0 270Z" fill="var(--gold)"/>
    </svg>
    <div class="back-brand">
      <div class="brand-ring"></div>
      <div class="brand-name">VENTURO MANE STUDIO</div>
    </div>
    <div class="services">
      <h2>OUR SERVICES</h2>
      <ul>
        <li>Custom Haircuts</li>
        <li>Coloring</li>
        <li>Extensions</li>
        <li>And Barbering</li>
        <li>Beard Grooming</li>
      </ul>
    </div>
  </section>
</main>
</body>
</html>
```